Contemporary Elegant Business Card Design for an International Trade Company in the Wine Industry

We need a new business card design for an international trade company in the wine and winemaking industry. The overall feel of the card should be contemporary, upscale, luxurious and elegant. It should communicate confidence and professionalism. The colors should complementary to our logo design (burgundy, gold, and black).
Inspiration: rich velvet tapestry
The card should include the following information:
Business: Brovenna Trading/Shipping, LLC.
Name: Marcus T. Hollenbrand
Title: CEO
Email: mark@brovennatrading.example
Phone: 555-294-6172
www.brovennatrading.example
Updates
Project Deadline Extended
Reason: We'd like the designers that we requested some additional designs from to still submit designs. Thank you!
Industry/Entity Type
Business
Contact Information for Business Card
Title: CEO
Phone: 555-294-6172
www.brovennatrading.example
Look and feel

```html
<!DOCTYPE html>
<html lang="en">
<head>
<meta charset="utf-8">
<title>Brovenna Trading/Shipping — Business Card</title>
<link href="https://fonts.googleapis.com/css2?family=Lato:wght@400;900&display=swap" rel="stylesheet">
<style>
  :root {
    --backdrop-top: #2a2a2a;
    --backdrop-bottom: #050505;
    --card-white: #f3f3f3;
    --gold: #c8922a;
    --gold-card: #d3962f;
    --gold-light: #d89d38;
    --gold-shade: #c88b2d;
    --burgundy: #7a1620;
    --ink: #333333;
    --black: #0d0d0d;
  }
  * { margin: 0; padding: 0; box-sizing: border-box; }
  html, body { width: 1200px; height: 900px; overflow: hidden; }
  body {
    position: relative;
    background: linear-gradient(180deg, var(--backdrop-top) 0%, #1a1a1a 45%, var(--backdrop-bottom) 100%);
    font-family: "Lato", sans-serif;
  }
  .card {
    position: absolute;
    top: 184px;
    height: 491px;
    border-radius: 14px;
    overflow: hidden;
  }
  .card-front {
    left: 299px;
    width: 301px;
    background: var(--card-white);
  }
  .card-back {
    left: 645px;
    width: 305px;
    background: var(--gold-card);
  }

  /* Front */
  .brand-block {
    position: absolute;
    left: 65px;
    top: 23px;
    width: 176px;
    display: flex;
    flex-direction: column;
    align-items: center;
  }
  .brand-square {
    width: 176px;
    height: 176px;
    background: var(--burgundy);
  }
  .brand-name {
    margin-top: 6px;
    font-weight: 900;
    font-size: 27px;
    letter-spacing: 0.5px;
    line-height: 32px;
    color: var(--black);
  }
  .person {
    position: absolute;
    top: 302px;
    left: 0;
    width: 100%;
    text-align: center;
  }
  .person-name {
    font-size: 18px;
    color: var(--gold);
    letter-spacing: 0.2px;
    text-transform: uppercase;
  }
  .person-title {
    margin-top: 2px;
    font-size: 13px;
    color: var(--burgundy);
    text-transform: uppercase;
  }
  .contact {
    position: absolute;
    top: 398px;
    left: 0;
    width: 100%;
    list-style: none;
    font-size: 14px;
    color: var(--ink);
    line-height: 20px;
  }
  .contact li { display: flex; justify-content: center; align-items: center; gap: 7px; }
  .contact svg { width: 11px; height: 9px; fill: var(--gold); }
  .contact .email { gap: 12px; }

  /* Back */
  .back-field {
    position: absolute;
    left: 0; top: 0;
    width: 305px;
    height: 339px;
  }
  .back-name {
    position: absolute;
    left: 0;
    top: 362px;
    width: 100%;
    text-align: center;
    font-weight: 900;
    font-size: 44px;
    letter-spacing: 1px;
    line-height: 52px;
    color: var(--black);
  }
</style>
</head>
<body>

  <section class="card card-front" aria-label="Business card front">
    <div class="brand-block">
      <div class="brand-square"></div>
      <div class="brand-name">BROVENNA</div>
    </div>

    <div class="person">
      <p class="person-name">Marcus T. Hollenbrand</p>
      <p class="person-title">CEO</p>
    </div>

    <ul class="contact">
      <li class="phone">
        <svg viewBox="0 0 11 9" aria-hidden="true"><path d="M1 3 C1 1 10 1 10 3 L8.5 4 L7.5 3 L3.5 3 L2.5 4 Z M2.5 5 L8.5 5 L9.5 8.5 L1.5 8.5 Z"/></svg>
        555-294-6172
      </li>
      <li class="email">
        <svg viewBox="0 0 11 9" aria-hidden="true"><path d="M0.5 1 L10.5 1 L5.5 5 Z M0.5 2.2 L5.5 6.2 L10.5 2.2 L10.5 8 L0.5 8 Z"/></svg>
        mark@brovennatrading.example
      </li>
      <li class="website">www.brovennatrading.example</li>
    </ul>
  </section>

  <section class="card card-back" aria-label="Business card back">
    <svg class="back-field" viewBox="0 0 305 339" aria-hidden="true">
      <defs>
        <linearGradient id="upperTone" x1="0" y1="0" x2="1" y2="1">
          <stop offset="0" stop-color="#dba241"/>
          <stop offset="1" stop-color="#d39836"/>
        </linearGradient>
      </defs>
      <rect class="lower-triangle-fill" x="0" y="0" width="305" height="339" fill="var(--gold-shade)"/>
      <polygon class="upper-triangle" points="0,0 305,0 305,316 0,14" fill="url(#upperTone)" role="img" aria-label="Faint antique world map in warm gold tones"/>
      <polygon class="lower-triangle" points="0,14 305,316 305,339 0,339" fill="var(--gold-shade)"/>
    </svg>
    <div class="back-name">BROVENNA</div>
  </section>

</body>
</html>
```